Landing page for a cyber security service provider called 'Quill Vantor'

The client is a new cyber security company in need of a website landing page at quillvantor.com.

Their visual identity is modern, playful, clean and uncluttered and represents innovation, connectivity and approachability.

The company logo is provided in black (attached) but the client is open to changing the colour to align with the new website design.

The landing page needs to contain:
- A call to action with a 'Get Started' button
-Links to blank 'How it works', 'Products', 'Pricing', 'About Us' and 'Contact Us' pages (that we'll fill out later)

Target Market(s)

Medium to large businesses who probably don't understand cyber / cyber security but need their business to be protected.

Industry/Entity Type

Cyber Security

Coding

Coded - Design and coding required

Number of Pages Required

1 page

Font styles to use
Sans Serif
Other font styles liked:
• Helvetica

Requirements
Nice to have
• Hero banner at the top of the landing page.
Should not have
• Should not look like a traditional cyber / cyber security design (eg no dark blue/ black, red/black colour combinations). Please no military styles (eg no shields, cannons, swords, guns)

```html
<!DOCTYPE html>
<html lang="en">
<head>
<meta charset="UTF-8">
<title>Quill Vantor — Next-Gen Cyber Security</title>
<link rel="stylesheet" href="https://fonts.googleapis.com/css2?family=Poppins:wght@400;500;600;700&display=swap">
<style>
:root{
  --orange:#f15a24;
  --orange-soft:#ff7a3d;
  --ink:#1c1b1f;
  --ink-2:#232226;
  --hero:#2a1810;
  --text:#222;
  --muted:#6b6b6b;
  --card:#f3f3f3;
  --band:#f1f0f0;
  --white:#fff;
}
*{margin:0;padding:0;box-sizing:border-box}
html,body{width:1200px;height:4736px;overflow:hidden}
body{position:relative;font-family:"Poppins",Helvetica,Arial,sans-serif;color:var(--text);background:var(--white)}
a{text-decoration:none;color:inherit}
.section{position:absolute;left:0;width:1200px}

/* top bar */
.topbar{top:0;height:40px;background:var(--ink);color:#fff;font-size:13px;display:flex;align-items:center;justify-content:center;gap:12px}
/* nav */
.nav{top:40px;height:83px;background:#fff}
.nav-links{position:absolute;left:368px;top:0;height:83px;display:flex;align-items:center;gap:38px;font-size:14px;font-weight:500;color:#333}
.nav-links .active{color:var(--orange);font-weight:600;position:relative}
.nav-links .active::after{content:"";position:absolute;left:50%;bottom:-26px;width:7px;height:7px;margin-left:-3px;border-radius:50%;background:var(--orange)}
.btn-contact{position:absolute;left:981px;top:21px;width:127px;height:40px;border-radius:4px;background:linear-gradient(90deg,var(--orange),var(--orange-soft));color:#fff;font-size:13px;font-weight:600;display:flex;align-items:center;justify-content:center;box-shadow:0 4px 10px rgba(241,90,36,.3)}
.logo-tab{position:absolute;left:108px;top:40px;width:148px;height:132px;background:#fff;border-radius:0 0 28px 28px;z-index:3;display:flex;flex-direction:column;align-items:center;justify-content:center;gap:8px}
.logo-dot{width:26px;height:26px;border-radius:50%;background:var(--orange)}
.logo-name{font-size:20px;font-weight:700;color:var(--ink);letter-spacing:.2px}

/* hero */
.hero{top:123px;height:542px;background:
  radial-gradient(ellipse 420px 260px at 330px 80px,rgba(241,90,36,.45),transparent 70%),
  radial-gradient(ellipse 500px 300px at 900px 300px,rgba(120,40,20,.6),transparent 70%),
  linear-gradient(120deg,#3a2014 0%,var(--hero) 45%,#1d110b 100%);color:#fff}
.hero h1{position:absolute;left:114px;top:118px;font-weight:700}
.hero h1 .l1{display:block;font-size:70px;line-height:80px}
.hero h1 .l2{display:block;font-size:52px;line-height:66px}
.hero .lead{position:absolute;left:114px;top:344px;font-size:15px;font-weight:600}
.btn-white{position:absolute;left:114px;top:397px;width:127px;height:39px;background:#fff;color:var(--ink);border-radius:4px;font-size:13px;font-weight:600;display:flex;align-items:center;justify-content:center}
.hero-art{position:absolute;left:698px;top:24px;width:332px;height:404px;border-radius:50%;background:
  radial-gradient(circle at 50% 45%,#f08a3c 0%,#a8502a 30%,#5a3028 55%,#2b1a16 75%,transparent 78%)}
.scroll-ring{position:absolute;left:993px;top:603px;width:124px;height:124px;border-radius:50%;background:var(--hero);z-index:2;display:flex;align-items:center;justify-content:center}
.scroll-btn{width:76px;height:76px;border-radius:50%;background:linear-gradient(180deg,var(--orange-soft),#c8421a);border:2px solid #f6b08f;display:flex;align-items:center;justify-content:center}

/* partners */
.partners{top:665px;height:245px;background:var(--band)}
.partners p{position:absolute;top:71px;width:100%;text-align:center;font-size:17px;font-weight:600;color:#333}
.partner-row{position:absolute;top:138px;width:100%;display:flex;justify-content:center;gap:44px}
.partner{display:flex;align-items:center;gap:7px;font-size:15px;font-weight:600;color:var(--orange)}
.partner i{width:14px;height:14px;border-radius:50%;background:var(--orange)}

/* why */
.why{top:910px;height:943px;background:#fff}
.h2{font-size:38px;font-weight:700;color:var(--ink);line-height:52px}
.why .h2.title{position:absolute;left:114px;top:62px}
.why .intro{position:absolute;left:621px;top:58px;width:460px;font-size:13px;line-height:20px;color:#444}
.deco-lines{position:absolute;background:radial-gradient(ellipse at center,rgba(241,90,36,.28),rgba(241,90,36,0) 70%)}
.feature{position:absolute;top:200px;width:300px;text-align:center}
.feature .ico{width:70px;height:70px;margin:0 auto;display:block}
.feature h3{margin-top:44px;font-size:21px;font-weight:700;color:var(--orange)}
.feature p{margin-top:12px;font-size:13px;line-height:20px;color:#555}
.value-title{position:absolute;left:114px;top:472px}
.value-text{position:absolute;left:114px;top:588px;width:290px;font-size:13px;line-height:20px;color:#555}
.link-more{position:absolute;display:flex;align-items:center;gap:22px;color:var(--orange);font-size:13px;font-weight:500}
.stat{position:absolute;width:200px}
.stat .lbl{font-size:18px;font-weight:600;color:var(--ink);line-height:22px}
.stat .num{margin-top:24px;font-size:54px;font-weight:700;color:var(--orange);line-height:60px;margin-left:-4px}
.stat .bar{margin-top:12px;width:198px;height:5px;background:#d9d9d9;position:relative}
.stat .bar span{position:absolute;left:0;top:0;height:5px;background:var(--orange)}
.stat .desc{margin-top:12px;font-size:14px;line-height:22px;color:#555}

/* how */
.how{top:1853px;height:514px;background:var(--ink);color:#fff}
.how h2{position:absolute;left:114px;top:70px;font-size:38px;font-weight:600}
.how .p{position:absolute;left:114px;top:124px;font-size:13px;line-height:20px;color:#ddd}
.step{position:absolute;left:114px}
.step h4{font-size:22px;font-weight:600}
.step p{margin-top:8px;font-size:13px;color:#ddd}
.how-img{position:absolute;left:675px;top:55px;width:406px;height:395px;border-radius:8px;background:
  radial-gradient(ellipse 260px 90px at 40% 92%,rgba(255,150,40,.95),transparent 70%),
  radial-gradient(ellipse 200px 160px at 65% 45%,rgba(70,90,110,.8),transparent 70%),
  linear-gradient(160deg,#3a3a42,#1a1a1f 60%,#5a2a10)}

/* solutions */
.solutions{top:2367px;height:596px;background:#fff}
.center-title{position:absolute;width:100%;text-align:center;font-size:38px;font-weight:600;color:var(--ink)}
.center-sub{position:absolute;width:100%;text-align:center;font-size:13px;color:#555}
.sol-card{position:absolute;top:191px;width:314px;height:324px;background:var(--card);border-radius:4px;text-align:center}
.sol-card .circle{width:96px;height:96px;border-radius:50%;background:#fff;margin:44px auto 0;display:flex;align-items:center;justify-content:center}
.sol-card h3{margin-top:36px;font-size:22px;font-weight:700;color:var(--orange)}
.sol-card p{margin:12px auto 0;width:270px;font-size:13px;line-height:20px;color:#555}
.sol-card .tick{position:absolute;left:107px;bottom:0;width:100px;height:5px;background:var(--orange);border-radius:3px 3px 0 0}

/* pricing */
.pricing-band{position:absolute;left:72px;top:2963px;width:1056px;height:349px;background:var(--ink);border-radius:6px;color:#fff;text-align:center}
.pricing-band h2{margin-top:62px;font-size:38px;font-weight:600}
.pricing-band p{margin-top:10px;font-size:13px;line-height:20px;color:#eee}
.plan{position:absolute;top:3171px;width:314px;height:477px;background:var(--card);border-radius:4px;padding:0 25px}
.plan.best{background:linear-gradient(170deg,#f26a2c,#e24e1c);color:#fff}
.plan .name{margin-top:38px;font-size:19px;font-weight:600;line-height:28px}
.plan .price{margin-top:10px;font-size:46px;font-weight:700;color:var(--orange);line-height:54px}
.plan .svc{font-size:20px;font-weight:700;color:var(--orange);line-height:26px}
.plan.best .price,.plan.best .svc{color:#fff}
.plan ul{list-style:none;margin-top:34px}
.plan li{font-size:11.5px;line-height:37px;color:#555;display:flex;align-items:center;gap:14px}
.plan.best li{color:#fff}
.plan li::before{content:"";width:0;height:0;border-left:8px solid var(--orange);border-top:5px solid transparent;border-bottom:5px solid transparent}
.plan.best li::before{border-left-color:#fff}
.plan .btn{position:absolute;left:93px;top:407px;width:128px;height:36px;border-radius:4px;background:linear-gradient(90deg,var(--orange),var(--orange-soft));color:#fff;font-size:13px;font-weight:600;display:flex;align-items:center;justify-content:center}
.plan.best .btn{background:#fff;color:var(--ink)}

/* news */
.news-card{position:absolute;top:3817px;width:314px;height:480px;background:var(--card);border-radius:4px;overflow:hidden}
.news-card .img{height:263px;position:relative}
.news-card .img::after{content:"";position:absolute;left:107px;bottom:0;width:100px;height:5px;background:var(--orange)}
.news-card h3{margin:24px 25px 0;font-size:18px;font-weight:600;line-height:27px;color:var(--ink)}
.news-card p{margin:12px 25px 0;font-size:13px;line-height:20px;color:#555}
.news-card .link-more{left:25px;top:438px}

/* footer */
.footer-bar{position:absolute;left:244px;top:4356px;width:712px;height:8px;background:var(--orange);border-radius:6px 6px 0 0}
.footer{top:4363px;height:373px;background:var(--ink);color:#fff}
.f-logo{position:absolute;left:114px;top:52px;display:flex;flex-direction:column;align-items:flex-start;gap:8px}
.f-logo .logo-dot{width:30px;height:30px}
.f-logo .logo-name{color:#fff;font-size:22px}
.f-about{position:absolute;left:114px;top:145px;width:240px;font-size:12px;line-height:15px;color:#ddd}
.f-col{position:absolute;top:94px}
.f-col h4{font-size:18px;font-weight:600;color:var(--orange);line-height:26px}
.f-col ul{list-style:none;margin-top:20px}
.f-col li{font-size:13px;line-height:37px}
.f-contact li{display:flex;align-items:center;gap:14px;font-size:14px;line-height:43px}
.f-line{position:absolute;left:114px;top:318px;width:950px;height:1px;background:#888}
.chat{position:absolute;left:1070px;top:300px;width:36px;height:36px;border-radius:50%;background:var(--orange);display:flex;align-items:center;justify-content:center}
.copy{position:absolute;top:337px;width:100%;text-align:center;font-size:12px;color:#ddd}
</style>
</head>
<body>

<div class="section topbar">Experiencing a Quill Vantor security incident? Get help now.
  <svg width="28" height="10" viewBox="0 0 28 10"><path d="M0 5h26M21 1l5 4-5 4" stroke="#fff" stroke-width="1.4" fill="none"/></svg>
</div>

<header class="section nav">
  <nav class="nav-links">
    <a class="active" href="#">Home</a>
    <a href="#">How It Work</a>
    <a href="#">Products</a>
    <a href="#">Pricing</a>
    <a href="#">About Us</a>
  </nav>
  <a class="btn-contact" href="#">Contact Us</a>
</header>
<div class="logo-tab"><span class="logo-dot"></span><span class="logo-name">Quill Vantor</span></div>

<section class="section hero">
  <h1><span class="l1">Next-Gen</span><span class="l2">Cyber Security for</span><span class="l2">Modern Businesses</span></h1>
  <p class="lead">Stay Ahead of Threats with Cutting-Edge, User-Friendly Solutions</p>
  <a class="btn-white" href="#">Get Started</a>
  <div class="hero-art" role="img" aria-label="Glowing circuit emblem with a padlock at its centre and orange accent spheres"></div>
</section>
<div class="scroll-ring"><div class="scroll-btn">
  <svg width="26" height="24" viewBox="0 0 26 24"><path d="M4 4l9 8 9-8M4 12l9 8 9-8" stroke="#fff" stroke-width="2" fill="none"/></svg>
</div></div>

<section class="section partners">
  <p>We are providing cybersecurity services to some of the World’s leading companies</p>
  <div class="partner-row">
    <span class="partner"><i></i>Norvale</span>
    <span class="partner"><i></i>Brightmesh</span>
    <span class="partner"><i></i>Kestrel</span>
    <span class="partner"><i></i>Ombrix</span>
    <span class="partner"><i></i>Tallow</span>
    <span class="partner"><i></i>Lumora</span>
    <span class="partner"><i></i>Corvant</span>
  </div>
</section>

<section class="section why">
  <h2 class="h2 title">Why Quill Vantor</h2>
  <p class="intro">Welcome to Quill Vantor, where innovation meets simplicity in cybersecurity. We offer state-of-the-art solutions tailored to protect medium and large businesses from today’s evolving threats.</p>
  <div class="deco-lines" role="img" aria-label="Flowing orange line waves" style="left:1040px;top:40px;width:160px;height:260px"></div>

  <div class="feature" style="left:116px">
    <svg class="ico" viewBox="0 0 70 70"><path d="M18 34a10 10 0 0 1 4-19 14 14 0 0 1 26 3 9 9 0 0 1 2 16z" fill="#222"/><rect x="27" y="40" width="16" height="13" rx="2" fill="var(--orange)"/><path d="M30 40v-4a5 5 0 0 1 10 0v4" stroke="#222" stroke-width="2.5" fill="none"/><path d="M20 60h30M35 53v7" stroke="#222" stroke-width="2"/></svg>
    <h3>AI-Powered Protection</h3>
    <p>Leverage advanced machine learning to<br>detect and mitigate threats in real-time.</p>
  </div>
  <div class="feature" style="left:449px">
    <svg class="ico" viewBox="0 0 70 70"><rect x="20" y="20" width="30" height="30" rx="4" fill="none" stroke="#222" stroke-width="2.5"/><rect x="26" y="26" width="18" height="18" rx="2" fill="var(--orange)"/><text x="35" y="39" font-size="10" font-family="Poppins,sans-serif" font-weight="700" fill="#fff" text-anchor="middle">AI</text><path d="M28 20v-8M35 20v-8M42 20v-8M28 50v8M35 50v8M42 50v8M20 28h-8M20 35h-8M20 42h-8M50 28h8M50 35h8M50 42h8" stroke="#222" stroke-width="2"/></svg>
    <h3>Cloud Security Solutions</h3>
    <p>Safeguard your cloud infrastructure with our<br>comprehensive, scalable security solutions.</p>
  </div>
  <div class="feature" style="left:780px">
    <svg class="ico" viewBox="0 0 70 70"><circle cx="35" cy="35" r="26" fill="none" stroke="#222" stroke-width="3"/><circle cx="35" cy="35" r="17" fill="none" stroke="var(--orange)" stroke-width="4"/><circle cx="35" cy="33" r="6" fill="#222"/><path d="M26 46a9 9 0 0 1 18 0" fill="#222"/></svg>
    <h3>User-Centric Design</h3>
    <p>Easy-to-use interfaces and seamless<br>integration with your existing systems.</p>
  </div>

  <h2 class="h2 value-title">The Value of<br>One Platform</h2>
  <p class="value-text">Consolidate products, maximize value, and improve business continuity. See why 4 of the top 10 global enterprises choose the Quill Vantor platform over other security vendors.</p>
  <a class="link-more" href="#" style="left:114px;top:804px">Get A Demo
    <svg width="50" height="10" viewBox="0 0 50 10"><path d="M0 5h48M43 1l5 4-5 4" stroke="var(--orange)" stroke-width="1.4" fill="none"/></svg></a>

  <div class="stat" style="left:608px;top:476px"><div class="lbl">Reduce Risk</div><div class="num">91%</div><div class="bar"><span style="width:82%"></span></div><div class="desc">Faster MTTR with no delayed detections</div></div>
  <div class="stat" style="left:856px;top:476px"><div class="lbl">Reduce Costs</div><div class="num">66%</div><div class="bar"><span style="width:68%"></span></div><div class="desc">Reduction in operational costs</div></div>
  <div class="stat" style="left:608px;top:700px"><div class="lbl">Maximize Value</div><div class="num">50%</div><div class="bar"><span style="width:50%"></span></div><div class="desc">Savings in data retention costs</div></div>
  <div class="stat" style="left:856px;top:700px"><div class="lbl">Increase Efficiency</div><div class="num">90%</div><div class="bar"><span style="width:88%"></span></div><div class="desc">Improvement in automation</div></div>
</section>

<section class="section how">
  <h2>How It Works</h2>
  <p class="p">Our approach combines advanced technology with expert analysis.<br>Here’s a quick overview of our process:</p>
  <div class="step" style="top:210px"><h4>Assessment</h4><p>Leverage advanced machine learning to detect and mitigate threats in real-time.</p></div>
  <div class="step" style="top:296px"><h4>Implementation</h4><p>Deploy our solutions to safeguard your data and infrastructure.</p></div>
  <div class="step" style="top:382px"><h4>Monitoring</h4><p>Continuous surveillance and updates to ensure ongoing protection.</p></div>
  <div class="how-img" role="img" aria-label="Laptop on a desk with a glowing padlock interface and streaks of orange light"></div>
</section>

<section class="section solutions">
  <div class="deco-lines" role="img" aria-label="Flowing orange line waves" style="left:0;top:4px;width:140px;height:276px"></div>
  <h2 class="center-title" style="top:66px">Our Solutions</h2>
  <p class="center-sub" style="top:132px">Explore our diverse range of cybersecurity solutions designed to meet your needs</p>

  <div class="sol-card" style="left:112px">
    <div class="circle"><svg width="56" height="56" viewBox="0 0 56 56"><rect x="16" y="16" width="24" height="24" rx="3" fill="none" stroke="#222" stroke-width="2"/><rect x="22" y="26" width="12" height="9" rx="1.5" fill="var(--orange)"/><path d="M24 26v-3a4 4 0 0 1 8 0v3" stroke="var(--orange)" stroke-width="2" fill="none"/><path d="M22 16V8M34 16V8M22 40v8M34 40v8M16 22H8M16 34H8M40 22h8M40 34h8" stroke="#222" stroke-width="2"/></svg></div>
    <h3>Endpoint Security</h3>
    <p>Protect individual devices from malware and cyber threats.</p>
    <span class="tick"></span>
  </div>
  <div class="sol-card" style="left:443px">
    <div class="circle"><svg width="56" height="56" viewBox="0 0 56 56"><circle cx="28" cy="30" r="9" fill="none" stroke="#222" stroke-width="2"/><path d="M19 30h18M28 21v18" stroke="#222" stroke-width="1.5"/><circle cx="12" cy="12" r="5" fill="#222"/><circle cx="44" cy="12" r="5" fill="#222"/><circle cx="12" cy="46" r="4" fill="var(--orange)"/><circle cx="44" cy="46" r="4" fill="var(--orange)"/><path d="M16 16l6 7M40 16l-6 7M15 43l6-6M41 43l-6-6" stroke="var(--orange)" stroke-width="1.6"/></svg></div>
    <h3>Network Security</h3>
    <p>Ensure the integrity and security of your network with our advanced firewalls and intrusion prevention systems.</p>
    <span class="tick"></span>
  </div>
  <div class="sol-card" style="left:774px">
    <div class="circle"><svg width="56" height="56" viewBox="0 0 56 56"><path d="M14 26a8 8 0 0 1 4-15 11 11 0 0 1 21 3 7 7 0 0 1 3 12z" fill="#222"/><circle cx="28" cy="36" r="12" fill="var(--orange)"/><path d="M22 36l4 4 8-8" stroke="#fff" stroke-width="2.5" fill="none"/></svg></div>
    <h3>Cloud Security</h3>
    <p>Guard your cloud assets with our comprehensive security services.</p>
    <span class="tick"></span>
  </div>
</section>

<section class="pricing-band">
  <h2>Pricing Plans</h2>
  <p>Discover our competitive pricing options tailored to fit the size and needs of your business.<br>Choose the plan that best suits your requirements and budget.</p>
</section>

<div class="plan" style="left:112px">
  <div class="name">Basic</div><div class="price">$115,99/</div><div class="svc">Services</div>
  <ul><li>Lorem ipsum dolor sit amet consectetur</li><li>Lorem ipsum dolor sit amet consectetur</li><li>Lorem ipsum dolor sit amet consectetur</li><li>Lorem ipsum dolor sit amet consectetur</li><li>Lorem ipsum dolor sit amet consectetur</li></ul>
  <a class="btn" href="#">Get Started</a>
</div>
<div class="plan best" style="left:443px">
  <div class="name">Best Value</div><div class="price">$200,99/</div><div class="svc">Services</div>
  <ul><li>Lorem ipsum dolor sit amet consectetur</li><li>Lorem ipsum dolor sit amet consectetur</li><li>Lorem ipsum dolor sit amet consectetur</li><li>Lorem ipsum dolor sit amet consectetur</li><li>Lorem ipsum dolor sit amet consectetur</li></ul>
  <a class="btn" href="#">Get Started</a>
</div>
<div class="plan" style="left:774px">
  <div class="name">Premium</div><div class="price">$315,99/</div><div class="svc">Services</div>
  <ul><li>Lorem ipsum dolor sit amet consectetur</li><li>Lorem ipsum dolor sit amet consectetur</li><li>Lorem ipsum dolor sit amet consectetur</li><li>Lorem ipsum dolor sit amet consectetur</li><li>Lorem ipsum dolor sit amet consectetur</li></ul>
  <a class="btn" href="#">Get Started</a>
</div>

<h2 class="center-title" style="top:3720px">The Latest News From Us</h2>

<article class="news-card" style="left:112px">
  <div class="img" role="img" aria-label="Padlock and key resting on a blue keyboard" style="background:linear-gradient(160deg,#4a6a9c,#2d4470 55%,#c9b06a)"></div>
  <h3>How To Protect Threats<br>From Hackers</h3>
  <p>Lorem ipsum dolor sit amet, risus so a consectetur adipiscing elit. Tortor id aliquam dignissim risus</p>
  <a class="link-more" href="#">Read More <svg width="50" height="10" viewBox="0 0 50 10"><path d="M0 5h48M43 1l5 4-5 4" stroke="var(--orange)" stroke-width="1.4" fill="none"/></svg></a>
</article>
<article class="news-card" style="left:443px">
  <div class="img" role="img" aria-label="Keyboard enter key over a glowing orange circuit board" style="background:linear-gradient(150deg,#2a3a55 0%,#e89a1c 45%,#f5b43a 100%)"></div>
  <h3>How To Protect Threats<br>From Hackers</h3>
  <p>Lorem ipsum dolor sit amet, risus so a consectetur adipiscing elit. Tortor id aliquam dignissim risus</p>
  <a class="link-more" href="#">Read More <svg width="50" height="10" viewBox="0 0 50 10"><path d="M0 5h48M43 1l5 4-5 4" stroke="var(--orange)" stroke-width="1.4" fill="none"/></svg></a>
</article>
<article class="news-card" style="left:774px">
  <div class="img" role="img" aria-label="Red hexagon tiles with padlock and warning symbols on a blue background" style="background:radial-gradient(circle at 55% 55%,#d8302e 0 30%,transparent 31%),linear-gradient(150deg,#3aa7e0,#1e86c8)"></div>
  <h3>How To Protect Threats<br>From Hackers</h3>
  <p>Lorem ipsum dolor sit amet, risus so a consectetur adipiscing elit. Tortor id aliquam dignissim risus</p>
  <a class="link-more" href="#">Read More <svg width="50" height="10" viewBox="0 0 50 10"><path d="M0 5h48M43 1l5 4-5 4" stroke="var(--orange)" stroke-width="1.4" fill="none"/></svg></a>
</article>

<div class="footer-bar"></div>
<footer class="section footer">
  <div class="f-logo"><span class="logo-dot"></span><span class="logo-name">Quill Vantor</span></div>
  <p class="f-about">Lorem ipsum dolor sit amet, consectetur adipiscing elit. Tortor id aliquam dignissim risus</p>
  <div class="f-col" style="left:417px"><h4>Our Services</h4><ul><li>Endpoint Security</li><li>Network Security</li><li>Cloud Security</li></ul></div>
  <div class="f-col" style="left:658px"><h4>Page</h4><ul><li>About Us</li><li>Our Team</li><li>Pricing</li><li>Our Blog</li></ul></div>
  <div class="f-col f-contact" style="left:849px"><h4>Contact Us</h4>
    <ul>
      <li><svg width="22" height="22" viewBox="0 0 24 24"><path d="M5 3h4l2 5-3 2a11 11 0 0 0 6 6l2-3 5 2v4a2 2 0 0 1-2 2A17 17 0 0 1 3 5a2 2 0 0 1 2-2z" fill="none" stroke="var(--orange)" stroke-width="1.6"/></svg>+1 555 014 2290</li>
      <li><svg width="22" height="22" viewBox="0 0 24 24"><rect x="3" y="5" width="18" height="14" rx="2" fill="none" stroke="var(--orange)" stroke-width="1.6"/><path d="M3 7l9 6 9-6" fill="none" stroke="var(--orange)" stroke-width="1.6"/></svg>info@quillvantor.com</li>
      <li><svg width="22" height="22" viewBox="0 0 24 24"><path d="M12 22s7-7 7-12a7 7 0 0 0-14 0c0 5 7 12 7 12z" fill="none" stroke="var(--orange)" stroke-width="1.6"/><circle cx="12" cy="10" r="2.5" fill="none" stroke="var(--orange)" stroke-width="1.6"/></svg>Arden Tower 418, Lucerne</li>
    </ul>
  </div>
  <div class="f-line"></div>
  <div class="chat"><svg width="18" height="18" viewBox="0 0 24 24"><path d="M4 12a8 8 0 1 1 4 7l-4 1 1-4a8 8 0 0 1-1-4z" fill="none" stroke="#fff" stroke-width="1.8"/></svg></div>
  <p class="copy">©copyright 2024 Quill Vantor. All Right Reserved.</p>
</footer>

</body>
</html>
```